personal development e-book needs book cover design

We need a book design for a new personal development course called 'The Ember Resolve'.

The course offers insights into how people can overcome negative, fear based mindsets to create the ultimate mindset empowering them to achieve huge success in their lives.

To be included on cover:
Title: The Ember Resolve
Sub-title: Empower your mind to live fearlessly, creating a life full of wealth, health and success.

Reference information
– What book/course is about
Discover Ancient Ninja Secrets to create the ultimate mindset and unleash your inner ninja. The book explains how to create this mindset and more, including:
* Overcome guilt, fear and self-doubt
* Understand that the right mindset is more critical to your success than talent
* Break free from childhood programming that is holding you back
* Stop being the victim
* Take responsibility and take control of your life
* Understand that while you can be your own worst enemy, you can also be your own best friend
* Learn to love yourself
* Find success in all areas of your life
* Help and inspire others, instead of dragging them down

Target Market(s)

self-help niche. 40-55 year old.

Font styles to use
Other font styles liked:
• Asian fonts - for example 'Last Ninja'.

Colors
0592cd
33a6d7
3276b5
f04a50
ffffff
ec1f27
000000

Requirements
Must have
• A Ninja.
Nice to have
• If you can somehow convey the idea of mindset into the cover that would be good. The Ember Resolve is the ultimate mindset so I want the cover to be powerful and convey that sense to the reader. If you can build some intrigue into the image as well that would be fantastic.
• Quote pull-outs in the book are blue, so while its not necessary to have blue on the cover, it would be consistent with the colour scheme in the book. I have chosen some colours that could be used on the cover below. (white, black and greys are fine too). It really does depend on the design.
Should not have
• Just a stock image with text overlay will not be chosen. I want some originality please.

```html
<!DOCTYPE html>
<html lang="en">
<head>
<meta charset="UTF-8">
<title>The Ember Resolve – Book Cover</title>
<link rel="stylesheet" href="https://fonts.googleapis.com/css2?family=Bebas+Neue&family=Oswald:wght@700&display=swap">
<style>
  :root {
    --navy-deep: #0a1a4f;
    --navy: #14287a;
    --royal: #3276b5;
    --sky: #33a6d7;
    --cyan: #0592cd;
    --red: #ec1f27;
    --white: #ffffff;
    --silver: #b9c2d3;
    --backdrop: #e8e8e8;
  }
  * { margin: 0; padding: 0; box-sizing: border-box; }
  html, body {
    width: 1200px;
    height: 1000px;
    overflow: hidden;
    background: var(--backdrop);
  }
  .stage {
    width: 1200px;
    height: 1000px;
    display: flex;
    align-items: center;
    justify-content: center;
  }
  .cover {
    position: relative;
    width: 600px;
    height: 900px;
    background: linear-gradient(165deg, var(--navy) 0%, var(--navy-deep) 50%, #0c1d5e 100%);
    overflow: hidden;
    box-shadow: 0 10px 30px rgba(0,0,0,0.25);
  }
  .cover__tech-lines {
    position: absolute;
    left: 0;
    top: 0;
    width: 600px;
    height: 360px;
  }
  .cover__gears {
    position: absolute;
    left: 30px;
    top: 110px;
    width: 250px;
    height: 170px;
    border-radius: 85px;
    background:
      radial-gradient(circle at 30% 60%, rgba(200,208,222,0.85) 0%, rgba(150,162,185,0.55) 28%, transparent 48%),
      radial-gradient(circle at 70% 35%, rgba(200,208,222,0.75) 0%, rgba(140,155,180,0.45) 26%, transparent 46%);
  }
  .cover__ninja {
    position: absolute;
    left: 300px;
    top: 90px;
    width: 170px;
    height: 190px;
    border-radius: 50%;
    background: radial-gradient(ellipse at center, rgba(255,255,255,0.9) 0%, rgba(255,255,255,0.55) 35%, rgba(255,255,255,0) 70%);
  }
  .cover__title {
    font-family: "Bebas Neue", "Oswald", sans-serif;
    font-weight: 400;
    color: var(--sky);
  }
  .cover__title-article,
  .cover__title-main,
  .cover__title-second {
    position: absolute;
    left: 40px;
    display: block;
    line-height: 0.85;
    letter-spacing: 2px;
  }
  .cover__title-article {
    top: 362px;
    color: var(--white);
    font-size: 44px;
    letter-spacing: 1px;
  }
  .cover__title-main {
    top: 404px;
    font-size: 212px;
  }
  .cover__title-second {
    top: 590px;
    font-size: 176px;
  }
  .cover__subtitle {
    position: absolute;
    left: 42px;
    right: 30px;
    top: 756px;
    font-family: "Oswald", sans-serif;
    font-weight: 700;
    text-transform: uppercase;
    color: var(--red);
    line-height: 1.08;
  }
  .cover__subtitle-line { display: block; font-size: 27px; }
  .cover__subtitle-line--strong { font-size: 50px; line-height: 1.1; }
</style>
</head>
<body>
  <main class="stage">
    <section class="cover">
      <svg class="cover__tech-lines" viewBox="0 0 600 360" aria-hidden="true">
        <defs>
          <radialGradient id="glow" cx="0.62" cy="0.3" r="0.55">
            <stop offset="0" stop-color="#33a6d7" stop-opacity="0.6"/>
            <stop offset="0.5" stop-color="#3276b5" stop-opacity="0.25"/>
            <stop offset="1" stop-color="#14287a" stop-opacity="0"/>
          </radialGradient>
        </defs>
        <rect width="600" height="360" fill="url(#glow)"/>
        <g stroke="#33a6d7" stroke-opacity="0.45" stroke-width="1.5" fill="none">
          <line x1="0" y1="60" x2="600" y2="60"/>
          <line x1="180" y1="95" x2="600" y2="95"/>
          <line x1="260" y1="140" x2="600" y2="140"/>
          <line x1="60" y1="300" x2="420" y2="300"/>
          <line x1="300" y1="230" x2="600" y2="230"/>
        </g>
        <g fill="#7fc6e6" fill-opacity="0.75">
          <path d="M330 120 L430 60 L425 52 L455 48 L442 74 L437 67 L337 128 Z"/>
          <path d="M420 150 L520 75 L514 67 L546 60 L534 90 L528 82 L428 158 Z"/>
        </g>
      </svg>
      <div class="cover__gears" role="img" aria-label="Illustration of interlocking silver gears suggesting the workings of the mind"></div>
      <div class="cover__ninja" role="img" aria-label="White silhouette of a crouching ninja"></div>
      <h1 class="cover__title">
        <span class="cover__title-article">The</span>
        <span class="cover__title-main">Ember</span>
        <span class="cover__title-second">Resolve</span>
      </h1>
      <p class="cover__subtitle">
        <span class="cover__subtitle-line">Empower your mind to live fearlessly,</span>
        <span class="cover__subtitle-line">creating a life full of wealth,</span>
        <span class="cover__subtitle-line cover__subtitle-line--strong">health and success.</span>
      </p>
    </section>
  </main>
</body>
</html>
```